Tallyleaf Web Design

Create Website Design for Tallyleaf. Tallyleaf is online application for collaboration team work system (task list management). More concept design for this project please find attach file ("tallyleaf website concept.pdf") . But my concept is just describe minimal features not bind design

For tallyleaf logo, i had already attach files. But i had not decided what color i chose, so it's okay if you suggest logo color for your suitable website design.
Updates

Dear All Designer,

I like brisk carousel (http://quorvanlabs.example/brisk-carousel/),
may be your concept design can adjust with this concept.
but don't worry about script for brisk carousel, my team will be handle
You just make website design to suitable with brisk carousel

but if you had own website design concept are welcome

thanks

Target Market(s)

Business Company

Industry/Entity Type

Management

```html
<!DOCTYPE html>
<html lang="en">
<head>
<meta charset="utf-8">
<title>Tallyleaf – Customize Online Collaboration Team Work</title>
<link href="https://fonts.googleapis.com/css2?family=Arimo:wght@400;700&display=swap" rel="stylesheet">
<style>
  :root {
    --header-bg: #f2f2f2;
    --brand-ink: #1f4a52;
    --nav-bg: #13292f;
    --nav-text: #ffffff;
    --green-top: #7aa92e;
    --green-bottom: #5b8a1d;
    --green-edge: #4b7414;
    --blue-top: #3b72ab;
    --blue-bottom: #20558c;
    --blue-edge: #1a4672;
    --hero-bg: #f2f2f2;
    --hero-title: #22507f;
    --body-light: #2f6a77;
    --body-dark: #1c4550;
    --accent-cyan: #5fd3ec;
    --panel-bg: #10282f;
    --rule: #3f7c88;
    --footer-text: #4fb0c9;
  }
  * { margin: 0; padding: 0; box-sizing: border-box; }
  html, body { width: 1200px; height: 1000px; overflow: hidden; }
  body {
    font-family: "Arimo", Arial, sans-serif;
    background: radial-gradient(ellipse 700px 600px at 600px 620px, var(--body-light), var(--body-dark));
    position: relative;
  }
  .site-header { position: absolute; top: 0; left: 0; width: 1200px; height: 75px; background: var(--header-bg); }
  .brand-name { position: absolute; left: 203px; top: 12px; font-size: 48px; font-weight: 700; color: var(--brand-ink); line-height: 1; letter-spacing: -1px; }
  .brand-tagline { position: absolute; left: 455px; top: 44px; font-size: 14px; font-weight: 700; color: var(--brand-ink); }
  .btn { position: absolute; top: 17px; height: 41px; border-radius: 4px; color: #fff; font-size: 14px; font-weight: 700; display: flex; align-items: center; justify-content: center; }
  .btn-login { left: 837px; width: 78px; background: linear-gradient(var(--green-top), var(--green-bottom)); border: 1px solid var(--green-edge); }
  .btn-signup { left: 922px; width: 78px; background: linear-gradient(var(--blue-top), var(--blue-bottom)); border: 1px solid var(--blue-edge); }
  .main-nav { position: absolute; top: 75px; left: 0; width: 1200px; height: 42px; background: var(--nav-bg); }
  .main-nav ul { list-style: none; position: absolute; right: 211px; top: 0; height: 42px; display: flex; align-items: center; gap: 32px; }
  .main-nav li { color: var(--nav-text); font-size: 14px; font-weight: 700; }
  .hero { position: absolute; top: 117px; left: 0; width: 1200px; height: 307px; background: var(--hero-bg); overflow: hidden; }
  .hero-photo { position: absolute; left: 0; top: 0; width: 640px; height: 307px;
    background: linear-gradient(90deg, #6c6a68 0%, #a9a39d 35%, #d9d3cd 70%, #f2f2f2 100%); }
  .hero-title { position: absolute; left: 614px; top: 42px; font-size: 45px; font-weight: 700; line-height: 50px; color: var(--hero-title); letter-spacing: -0.5px; }
  .hero-cta { position: absolute; left: 614px; top: 200px; width: 288px; height: 54px; border-radius: 3px; background: linear-gradient(var(--green-top), var(--green-bottom)); border: 1px solid var(--green-edge); color: #fff; font-size: 25px; font-weight: 700; display: flex; align-items: center; justify-content: center; }
  .slider-arrow { position: absolute; top: 125px; }
  .slider-arrow.prev { left: 60px; }
  .slider-arrow.next { left: 1114px; }
  .features { position: absolute; top: 424px; left: 200px; width: 800px; }
  .features-title { margin-top: 20px; text-align: center; font-size: 38px; font-weight: 700; color: var(--accent-cyan); text-shadow: 0 2px 3px rgba(0,0,0,0.45); line-height: 44px; }
  .rule { height: 1px; background: var(--rule); }
  .features .rule.top { margin-top: 13px; }
  .feature { position: absolute; top: 98px; }
  .feature-label { height: 42px; background: var(--panel-bg); color: var(--accent-cyan); font-size: 16px; font-weight: 700; display: flex; align-items: center; justify-content: center; }
  .feature-label.notch-left { clip-path: polygon(0 0, 100% 0, 100% 100%, 0 100%, 10px 50%); }
  .feature-label.notch-right { clip-path: polygon(0 0, 100% 0, calc(100% - 10px) 50%, 100% 100%, 0 100%); }
  .feature-card { margin-top: 13px; height: 135px; background: var(--panel-bg); display: flex; align-items: center; justify-content: center; box-shadow: 0 1px 0 rgba(95,211,236,0.15); }
  .feature-art { height: 90px; border-radius: 6px; background: radial-gradient(ellipse at center, rgba(95,211,236,0.35), rgba(95,211,236,0.08)); }
  .site-footer { position: absolute; top: 734px; left: 200px; width: 800px; }
  .site-footer p { margin-top: 21px; text-align: center; font-size: 11.5px; color: var(--footer-text); }
</style>
</head>
<body>
  <header class="site-header">
    <span class="brand-name">tallyleaf</span>
    <span class="brand-tagline">Customize Online Collaboration Team Work</span>
    <a class="btn btn-login">Login</a>
    <a class="btn btn-signup">Signup</a>
  </header>

  <nav class="main-nav">
    <ul>
      <li>Products</li>
      <li>Solutions</li>
      <li>Plans &amp; Pricing</li>
      <li>Help/Support</li>
      <li>Contact us</li>
    </ul>
  </nav>

  <section class="hero">
    <div class="hero-photo" role="img" aria-label="Photo of two business colleagues looking at a tablet together"></div>
    <h1 class="hero-title">Customize Online<br>Collaboration<br>Team Work</h1>
    <a class="hero-cta">Learn More</a>
    <svg class="slider-arrow prev" width="26" height="42" viewBox="0 0 26 42"><path d="M20 3 L6 21 L20 39" stroke="#fff" stroke-width="7" fill="none"/></svg>
    <svg class="slider-arrow next" width="26" height="42" viewBox="0 0 26 42"><path d="M6 3 L20 21 L6 39" stroke="#777" stroke-width="7" fill="none"/></svg>
  </section>

  <section class="features">
    <h2 class="features-title">The Greatness or Differences from Tallyleaf</h2>
    <div class="rule top"></div>

    <div class="feature" style="left:0;width:238px">
      <div class="feature-label notch-left">Customize Application</div>
      <div class="feature-card">
        <div class="feature-art" style="width:120px" role="img" aria-label="Line illustration of a folder with a user profile"></div>
      </div>
    </div>

    <div class="feature" style="left:277px;width:247px">
      <div class="feature-label">Synchronize All Device</div>
      <div class="feature-card">
        <div class="feature-art" style="width:156px" role="img" aria-label="Line illustration of a laptop and phone syncing through a cloud"></div>
      </div>
    </div>

    <div class="feature" style="left:563px;width:238px">
      <div class="feature-label notch-right">Report</div>
      <div class="feature-card" style="margin-top:15px">
        <div class="feature-art" style="width:104px" role="img" aria-label="Line illustration of report documents"></div>
      </div>
    </div>
  </section>

  <footer class="site-footer">
    <div class="rule"></div>
    <p>© 2013 Tallyleaf Trademarks belong to their respective owners. All rights reserved.</p>
  </footer>
</body>
</html>
```